Small corporate website template design

I need a couple templates designed for a small corporate website. The corporate site reflects the existence of the parent company which will own various brands/services that have their own websites, so it will mainly be used to present who we are, what we do, what is happening (news/events), how to contact us, link off to our other brand/service sites, as well as post information for public relations, investors, and job opportunities.

The company name is Vornelight LLC (www.vornelight.example), and the name is representative of stratified layers of interconnected digital services. The corporate site is not expected to generate a bunch of fanfare - that honor will be reserved for the externally linked brand/service sites.

The provided logo may be manipulated in color, size, shape, positioning, etc. to get it to fit with the design, but should be integrated in some way.

What we are looking for is a home page layout as well as a template for an inner page whereby the navigation/logo, etc may be diminished to some extent for the inner pages. We are also interested in reusable elements such as dividers, content containers, etc. in order to represent the types of information described above that we would like to present as described above.

We are particularly interested in consistency of design elements, conservative use of color (including consideration of accessibility concerns), judicious use of whitespace in favor of simplified messaging, and something lending itself well to internationalization/translation.

Target Market(s)

Small business owners, entrepreneurs (B2B)

Number of Pages Required

2 page

Font styles to use
Sans Serif

Requirements
Must have
• See the attached PDF with the logo concept, color swatches, and comparative sites.

```html
<!DOCTYPE html>
<html lang="en">
<head>
<meta charset="utf-8">
<title>Vornelight — Adaptive Software Technology</title>
<link rel="stylesheet" href="https://fonts.googleapis.com/css2?family=Montserrat:wght@300;400;600;700&family=Lato:wght@300;400;700&display=swap">
<style>
:root{
  --navy:#1b3a72;
  --navy-deep:#0e1c38;
  --blue:#2f63b2;
  --blue-mid:#3b70bf;
  --blue-text:#24508f;
  --orange:#f7941d;
  --ink:#1e1e1e;
  --grey:#8a8f98;
  --band:#e8eff8;
  --line:#e4e7ec;
  --white:#ffffff;
}
*{box-sizing:border-box;margin:0;padding:0}
html,body{width:1200px;height:2675px;overflow:hidden}
body{position:relative;background:var(--white);font-family:'Lato',Arial,sans-serif;color:var(--ink)}
.abs{position:absolute}
.backdrop{position:absolute;left:0;top:0}

/* header */
.brand{left:98px;top:52px;display:flex;align-items:center;gap:12px;font-family:'Montserrat',Arial,sans-serif;font-weight:700;font-size:24px;color:var(--white);letter-spacing:.5px}
.brand-mark{width:30px;height:30px;border-radius:50%;background:var(--white)}
.main-nav{left:484px;top:56px;display:flex;gap:0;font-family:'Montserrat',Arial,sans-serif;font-size:13px;color:var(--white)}
.main-nav a{color:inherit;text-decoration:none;position:absolute;white-space:nowrap}
.main-nav .active::after{content:"";position:absolute;left:0;right:0;top:26px;height:3px;background:var(--orange)}
.sign-in{left:993px;top:48px;width:108px;height:38px;border:2px solid var(--orange);border-radius:19px;color:var(--orange);font-family:'Montserrat',Arial,sans-serif;font-weight:600;font-size:13px;display:flex;align-items:center;justify-content:center;gap:6px}

.hero-title{left:98px;top:244px;font-family:'Montserrat',Arial,sans-serif;color:var(--white);font-size:44px;line-height:63px}
.hero-title b{font-weight:700;display:block}
.hero-title span{font-weight:300;display:block}
.btn{display:flex;align-items:center;justify-content:center;border-radius:22px;font-family:'Montserrat',Arial,sans-serif;font-weight:600;font-size:13px}
.btn-brands{left:98px;top:458px;width:139px;height:42px;background:var(--orange);color:var(--white)}
.btn-contact{left:246px;top:458px;width:132px;height:42px;background:var(--white);color:var(--orange)}
.slider-dots{left:98px;top:527px;display:flex;gap:10px}
.slider-dots i{width:15px;height:15px;border-radius:50%;background:var(--white)}
.slider-dots i.off{background:transparent;border:2px solid var(--white)}
.hero-visual{left:676px;top:108px;width:424px;height:482px}

/* who we are */
.who-title{right:710px;top:784px;display:flex;align-items:center;gap:20px;font-family:'Montserrat',Arial,sans-serif;font-weight:600;font-size:38px;color:var(--ink)}
.who-icon{width:64px;height:64px;border-radius:50%;background:var(--navy)}
.who-lead{right:712px;top:838px;font-size:17px;color:var(--blue-text);text-align:right}
.who-copy{left:96px;top:884px;width:476px;text-align:right;font-size:15px;line-height:33px;color:var(--grey);font-weight:300}
.btn-outline{left:462px;top:1064px;width:110px;height:40px;border:2px solid var(--orange);border-radius:20px;color:var(--orange);background:var(--white);font-family:'Montserrat',Arial,sans-serif;font-weight:600;font-size:12px;display:flex;align-items:center;justify-content:center}
.who-visual{left:600px;top:785px;width:502px;height:324px;background:radial-gradient(circle at 77% 65%,#3d78d6 0,#2e62c4 26%,rgba(46,98,196,.25) 40%,rgba(255,255,255,0) 62%)}

/* what we do */
.wwd-icon{left:572px;top:1316px;width:56px;height:56px;border-radius:50%;background:#e8553a}
.wwd-title{left:0;width:1200px;top:1388px;text-align:center;font-family:'Montserrat',Arial,sans-serif;font-weight:600;font-size:38px}
.wwd-lead{left:0;width:1200px;top:1444px;text-align:center;font-size:17px;color:var(--blue-text)}
.service-card{top:1510px;width:487px;height:145px;background:var(--white);box-shadow:0 2px 8px rgba(20,40,80,.12)}
.card-a{left:100px}
.card-b{left:613px}
.service-card .glyph{position:absolute;left:0;top:28px;width:72px;height:62px;border-radius:4px}
.card-a .glyph{background:#52b8c6}
.card-b .glyph{left:0;background:#2264c4}
.service-card h3{position:absolute;left:96px;top:24px;font-family:'Montserrat',Arial,sans-serif;font-weight:600;font-size:14px;color:var(--navy)}
.service-card p{position:absolute;left:96px;top:54px;width:360px;font-size:13px;line-height:25px;color:var(--grey);font-weight:300}
.service-card .more{position:absolute;right:30px;top:112px;font-size:11px;color:var(--blue);font-style:italic;text-decoration:underline}
.arrow{font-size:28px;color:var(--ink);font-weight:300;font-family:'Lato',Arial,sans-serif}

/* brands */
.brand-row{left:133px;top:1949px;display:flex;gap:9px}
.brand-tile{width:152px;height:72px;border:1px solid #dcdfe4;display:flex;align-items:center;justify-content:center;font-family:'Montserrat',Arial,sans-serif;font-weight:700;font-size:19px;color:#222}
.rule{left:98px;top:2083px;width:1004px;height:1px;background:var(--line)}

/* cta */
.cta-title{left:0;width:1200px;top:2154px;text-align:center;font-family:'Montserrat',Arial,sans-serif;font-weight:600;font-size:38px}
.cta-lead{left:0;width:1200px;top:2215px;text-align:center;font-size:17px;color:var(--blue-text)}
.signup{left:307px;top:2273px;width:585px;height:49px;border:1px solid #dcdfe4;border-radius:25px;background:var(--white)}
.signup .envelope{position:absolute;left:22px;top:17px}
.signup .field{position:absolute;left:52px;top:14px;font-size:15px;color:#9aa0a8}
.signup .send{position:absolute;right:4px;top:4px;width:111px;height:40px;border-radius:20px;background:var(--orange);color:var(--white);font-family:'Montserrat',Arial,sans-serif;font-weight:600;font-size:18px;display:flex;align-items:center;justify-content:center}

/* footer */
.foot-nav{left:173px;top:2573px;font-family:'Montserrat',Arial,sans-serif;font-size:13px;color:var(--white);word-spacing:2px}
.foot-nav .sep{margin:0 9px}
.copyright{left:176px;top:2607px;font-size:13px;color:#d9e0ec}
.foot-divider{left:727px;top:2530px;width:1px;height:110px;background:rgba(255,255,255,.25)}
.foot-brand{left:805px;top:2532px;width:220px;text-align:center;font-family:'Montserrat',Arial,sans-serif;font-weight:700;font-size:26px;color:var(--white);letter-spacing:1px}
.foot-brand .dot{display:block;width:40px;height:40px;margin:0 auto 14px;border-radius:50%;background:var(--white)}
</style>
</head>
<body>

<svg class="backdrop" width="1200" height="2675" viewBox="0 0 1200 2675" aria-hidden="true">
  <defs>
    <linearGradient id="heroFill" x1="0" y1="0" x2="0" y2="1">
      <stop offset="0" stop-color="#1c3e7a"/>
      <stop offset="1" stop-color="#3f72c2"/>
    </linearGradient>
    <linearGradient id="footFill" x1="0" y1="0" x2="0" y2="1">
      <stop offset="0" stop-color="#1a3466"/>
      <stop offset="1" stop-color="#0e1c38"/>
    </linearGradient>
  </defs>
  <polygon points="0,0 1200,0 1200,562 0,731" fill="url(#heroFill)"/>
  <polygon points="0,722 1200,553 1200,566 0,735" fill="#1b3a72"/>
  <polygon points="0,1275 1200,1132 1200,1738 0,1904" fill="#e8eff8"/>
  <polygon points="0,1262 600,1222 0,1282" fill="#2f63b2"/>
  <polygon points="0,1904 1200,1732 1200,1762 0,1912" fill="#2f63b2"/>
  <polygon points="0,2541 1200,2371 1200,2675 0,2675" fill="url(#footFill)"/>
  <polygon points="0,2533 1200,2363 1200,2380 0,2545" fill="#2f63b2"/>
</svg>

<header>
  <div class="abs brand"><span class="brand-mark"></span>VORNELIGHT</div>
  <nav class="abs main-nav">
    <a class="active" style="left:0">HOME</a>
    <a style="left:79px">WHO WE ARE</a>
    <a style="left:198px">WHAT WE DO</a>
    <a style="left:318px">NEWS &#709;</a>
    <a style="left:404px">CONTACT US</a>
  </nav>
  <div class="abs sign-in">
    <svg width="11" height="12" viewBox="0 0 11 12"><circle cx="5.5" cy="3" r="3" fill="#f7941d"/><path d="M0 12c0-4 2.5-5.5 5.5-5.5S11 8 11 12z" fill="#f7941d"/></svg>SIGN IN
  </div>
</header>

<section class="hero">
  <h1 class="abs hero-title"><b>Adaptive</b><b>Software Technology</b><span>for the Digital Revolution</span></h1>
  <div class="abs btn btn-brands">OUR BRANDS</div>
  <div class="abs btn btn-contact">CONTACT US</div>
  <div class="abs slider-dots"><i></i><i></i><i></i><i class="off"></i></div>
  <svg class="abs hero-visual" viewBox="0 0 424 482" role="img" aria-label="Illustration of a monitor surrounded by charts, dashboards and analytics icons inside a hexagon">
    <polygon points="212,0 424,120 424,362 212,482 0,362 0,120" fill="#1e4a92"/>
    <polygon points="212,14 410,128 410,354 212,468 14,354 14,128" fill="#4d83cf"/>
  </svg>
</section>

<section class="who">
  <h2 class="abs who-title">Who We Are<span class="who-icon"></span></h2>
  <p class="abs who-lead">At vero eos et accusamus et iusto odio dignissimos</p>
  <p class="abs who-copy">Sed ut perspiciatis unde omnis iste natus error sit voluptatem accusan-tium doloremque laudantium, totam rem aperiam, eaque ipsa quae ab illo inventore veritatis et quasi architecto beatae rem aperiam, eaque ipsa quae ab illo inventore veritatis et quasi architecto beatae vitae dicta sunt e vitae d rem aperiam, eaque ipsa quae ab illo inventore</p>
  <div class="abs btn-outline">READ MORE</div>
  <div class="abs who-visual" role="img" aria-label="Illustration of a sphere of blue pixel squares dispersing into scattered particles"></div>
</section>

<section class="what">
  <div class="abs wwd-icon"></div>
  <h2 class="abs wwd-title">What We Do</h2>
  <p class="abs wwd-lead">At vero eos et accusamus et iusto odio dignissimos ducimus qui blanditiiti</p>
  <div class="abs arrow" style="left:54px;top:1562px">&#8249;</div>
  <article class="abs service-card card-a">
    <span class="glyph"></span>
    <h3>ET QUASI ARCHITECTO</h3>
    <p>Sed ut perspiciatis unde omnis iste natus error sit voluptatem accusantium doloremque laudantium totam rem aperiam.</p>
    <span class="more">READ MORE &raquo;</span>
  </article>
  <article class="abs service-card card-b">
    <span class="glyph" style="left:0"></span>
    <h3>REPREHENDERIT QUI</h3>
    <p>Sed ut perspiciatis unde omnis iste natus error sit voluptatem accusantium doloremque laudantium totam rem aperiam.</p>
    <span class="more">READ MORE &raquo;</span>
  </article>
  <div class="abs arrow" style="left:1128px;top:1562px">&#8250;</div>
</section>

<section class="brands">
  <div class="abs arrow" style="left:95px;top:1966px">&#8249;</div>
  <div class="abs brand-row">
    <div class="brand-tile">Harbor Nine</div>
    <div class="brand-tile">Quillmark</div>
    <div class="brand-tile">Tessaline</div>
    <div class="brand-tile">Brightfen</div>
    <div class="brand-tile">Orchel</div>
    <div class="brand-tile">Lumaro</div>
  </div>
  <div class="abs arrow" style="left:1090px;top:1966px">&#8250;</div>
  <div class="abs rule"></div>
</section>

<section class="cta">
  <h2 class="abs cta-title">Ready to Get Started?</h2>
  <p class="abs cta-lead">At vero eos et accusamus et iusto odio dignissimos ducimus qui blanditiiti atque corrupti quos</p>
  <div class="abs signup">
    <svg class="envelope" width="20" height="14" viewBox="0 0 20 14"><rect width="20" height="14" rx="2" fill="#f7b36b"/><path d="M1 1l9 7 9-7" stroke="#fff" stroke-width="1.6" fill="none"/></svg>
    <span class="field">Type Your Email here</span>
    <span class="send">Send</span>
  </div>
</section>

<footer>
  <div class="abs foot-nav">HOME<span class="sep">/</span>WHO WE ARE<span class="sep">/</span>WHAT WE DO<span class="sep">/</span>NEWS<span class="sep">/</span>CONTACT US</div>
  <p class="abs copyright">© 2018 Vornelight. All rights reserved &nbsp;|&nbsp; Privacy policy</p>
  <div class="abs foot-divider"></div>
  <div class="abs foot-brand"><span class="dot"></span>VORNELIGHT</div>
</footer>

</body>
</html>
```